Business Card Design Project

I need a business card design for our new logo, please check the logo at the following link:
https://www.filecrate.net/s/q7rtx2pw9kd41m/FernLoop.png
The address on the business card:
Av. Gervásio Tavares 418 sala 207
Barra da Tijuca, Rio de Janeiro, RJ
CEP: 22714-380
Brasil
Phone: +55 21 86347215
e-mail: osvaldo@fernloop.com.br
Updates
Thank you all for sending your designs, we will not provide feedback because there are too many designs, on December 3 we will pick the best design according to our point of view. Please keep posting.
Osvaldo
Industry/Entity Type
Business
Look and feel
Each slider illustrates characteristics of the customer's brand and the style your logo design should communicate.

```html
<!DOCTYPE html>
<html lang="pt-BR">
<head>
<meta charset="utf-8">
<title>FernLoop – Cartão de visita</title>
<link rel="stylesheet" href="https://fonts.googleapis.com/css2?family=Heebo:wght@400;500;700;800&display=swap">
<style>
  :root {
    --page-bg: #e8e6e2;
    --card-yellow: #ecc018;
    --card-yellow-deep: #d9ab0c;
    --card-white: #f4f4f2;
    --ink: #1c1c1a;
    --rule: #2a2a26;
  }
  * { box-sizing: border-box; margin: 0; padding: 0; }
  html, body {
    width: 1200px;
    height: 880px;
    overflow: hidden;
    background: var(--page-bg);
    font-family: "Heebo", Arial, sans-serif;
    color: var(--ink);
  }
  .sheet {
    width: 1200px;
    height: 880px;
    display: flex;
    align-items: center;
    justify-content: space-evenly;
  }
  .card {
    position: relative;
    width: 540px;
    height: 310px;
    overflow: hidden;
    box-shadow: 0 10px 24px rgba(0,0,0,0.18);
  }

  /* Front */
  .card--front {
    background: var(--card-yellow);
    display: flex;
    flex-direction: column;
    align-items: center;
  }
  .brand {
    display: flex;
    align-items: center;
    gap: 12px;
  }
  .brand__dot {
    width: 22px;
    height: 22px;
    border-radius: 50%;
    background: var(--ink);
  }
  .brand__name {
    font-weight: 800;
    color: var(--ink);
    letter-spacing: -0.5px;
  }
  .card--front .brand { margin-top: 118px; }
  .card--front .brand__name { font-size: 60px; line-height: 1; }
  .front__rule {
    width: 380px;
    height: 2px;
    margin-top: 30px;
    background: linear-gradient(90deg, transparent, var(--rule) 20%, var(--rule) 80%, transparent);
    opacity: 0.75;
  }
  .front__web {
    margin-top: 12px;
    font-size: 17px;
    letter-spacing: 2.5px;
    font-weight: 400;
  }
  .front__web strong { font-weight: 700; }

  /* Back */
  .card--back { background: var(--card-white); }
  .back__band {
    position: absolute;
    inset: 0;
  }
  .card--back .brand {
    position: absolute;
    left: 44px;
    top: 60px;
  }
  .card--back .brand__name { font-size: 40px; line-height: 1; }
  .card--back .brand__dot { width: 16px; height: 16px; }
  .contact {
    position: absolute;
    right: 28px;
    top: 130px;
    text-align: right;
    font-size: 14px;
    line-height: 1.35;
  }
  .contact__name { font-size: 19px; font-weight: 700; }
  .contact__role { margin-bottom: 8px; }
  .contact__rule {
    width: 220px;
    height: 1px;
    margin: 8px 0 8px auto;
    background: var(--rule);
  }
</style>
</head>
<body>
<main class="sheet">

  <section class="card card--front" aria-label="Frente do cartão">
    <div class="brand">
      <span class="brand__dot"></span>
      <span class="brand__name">FernLoop</span>
    </div>
    <div class="front__rule"></div>
    <p class="front__web">www.<strong>fernloop</strong>.com.br</p>
  </section>

  <section class="card card--back" aria-label="Verso do cartão">
    <svg class="back__band" viewBox="0 0 540 310" role="img" aria-label="Faixa curva amarela decorativa no canto inferior direito">
      <defs>
        <linearGradient id="bandFill" x1="0" y1="0" x2="1" y2="1">
          <stop offset="0" stop-color="#f2cc2a"/>
          <stop offset="1" stop-color="#e3b20f"/>
        </linearGradient>
      </defs>
      <path d="M0 170 C 150 210 330 200 430 110 C 470 80 500 70 540 66 L 540 310 L 0 310 Z" fill="url(#bandFill)"/>
    </svg>
    <div class="brand">
      <span class="brand__dot"></span>
      <span class="brand__name">FernLoop</span>
    </div>
    <div class="contact">
      <p class="contact__name">Osvaldo Mendes</p>
      <p class="contact__role">CEO</p>
      <p>osvaldo@fernloop.com.br</p>
      <p>+55 21 86347215</p>
      <div class="contact__rule"></div>
      <p>Av. Gervásio Tavares 418 sala 207</p>
      <p>Barra da Tijuca, Rio de Janeiro, RJ</p>
      <p>CEP: 22714-380</p>
      <p>Brasil</p>
    </div>
  </section>

</main>
</body>
</html>
```